Harborne Cellarbook: the premier wine registry - (need business cards)

We have a logo designed, and now we need business cards for our 3 founders. Harborne Cellarbook is the premier wine registry for weddings. I am envisioning the wine glass with the heart in it as our signature symbol. (FYI- on the red background file, only use the part that has the red background; the brown colors are not relevant)

```html
<!DOCTYPE html>
<html lang="en">
<head>
<meta charset="utf-8">
<title>Harborne Cellarbook — Business Cards</title>
<link href="https://fonts.googleapis.com/css2?family=Montserrat:wght@400;500&display=swap" rel="stylesheet">
<style>
  :root {
    --page: #e9e5e0;
    --card: #96264c;
    --rule: #d9cfd3;
    --ink: #ffffff;
    --mark: #d6d2d3;
    --shadow: rgba(40, 20, 25, 0.35);
  }
  * { box-sizing: border-box; margin: 0; padding: 0; }
  html, body {
    width: 900px; height: 1200px; overflow: hidden;
    background: var(--page);
    font-family: "Montserrat", Arial, sans-serif;
    color: var(--ink);
  }
  .canvas { position: relative; width: 900px; height: 1200px; }
  .card {
    position: absolute; left: 97px; width: 706px; height: 410px;
    background: var(--card);
    box-shadow: 0 6px 16px var(--shadow);
  }
  .card--front { top: 167px; }
  .card--back { top: 614px; }
  .card__frame {
    position: absolute; left: 26px; top: 25px; right: 26px; bottom: 26px;
    border: 1.5px solid var(--rule);
  }
  .brand-name {
    position: absolute; color: var(--mark);
    font-weight: 400; text-transform: uppercase;
  }
  .card--front .brand-name {
    left: 80px; top: 172px; width: 236px;
    font-size: 25px; line-height: 34px; letter-spacing: 3px; text-align: center;
  }
  .card--back .brand-name {
    left: 0; right: 0; top: 200px; text-align: center;
    font-size: 31px; letter-spacing: 5px;
  }
  .divider {
    position: absolute; left: 335px; top: 113px; width: 1px; height: 185px;
    background: var(--rule);
  }
  .contact { position: absolute; left: 359px; top: 106px; }
  .contact__name { font-size: 20px; font-weight: 500; letter-spacing: 1px; line-height: 24px; }
  .contact__role { font-size: 14.5px; letter-spacing: 0.6px; line-height: 22px; margin-bottom: 12px; }
  .contact__line { display: flex; align-items: center; font-size: 15px; line-height: 22px; letter-spacing: 0.3px; }
  .contact__line svg { width: 15px; height: 15px; margin-right: 9px; fill: var(--ink); }
  .contact__address { margin-top: 10px; font-size: 15px; line-height: 22px; letter-spacing: 0.3px; }
</style>
</head>
<body>
<main class="canvas">
  <section class="card card--front">
    <div class="card__frame"></div>
    <div class="brand-name">Harborne<br>Cellarbook</div>
    <div class="divider"></div>
    <div class="contact">
      <div class="contact__name">DANIEL ASHWORTH</div>
      <div class="contact__role">MANAGING DIRECTOR</div>
      <div class="contact__line">
        <svg viewBox="0 0 16 16" aria-hidden="true"><path d="M2 5c0-2 3-3 6-3s6 1 6 3v1h-3V5H5v1H2zM4 7h8l2 6H2z"/></svg>
        555 014 2290
      </div>
      <div class="contact__line">
        <svg viewBox="0 0 16 16" aria-hidden="true"><path d="M1 3h14v2L8 9 1 5zM1 6.5l7 4 7-4V13H1z"/></svg>
        info@harbornecellarbook.com
      </div>
      <div class="contact__line">
        <svg viewBox="0 0 16 16" aria-hidden="true"><path d="M8 1a7 7 0 1 0 0 14A7 7 0 0 0 8 1zm0 1.5c.8 0 1.6 1.6 1.9 4H6.1C6.4 4.1 7.2 2.5 8 2.5zM2.6 7.5h2.5c0 .3 0 .7 0 1H2.6zm8.3 0h2.5v1h-2.5c0-.3 0-.7 0-1zm-4.8 2h3.8c-.3 2.4-1.1 4-1.9 4s-1.6-1.6-1.9-4z"/></svg>
        www.harbornecellarbook.com
      </div>
      <div class="contact__address">118 Linden Court NW<br>Suite 210, Fairhaven<br>OR 97401</div>
    </div>
  </section>

  <section class="card card--back">
    <div class="card__frame"></div>
    <div class="brand-name">Harborne Cellarbook</div>
  </section>
</main>
</body>
</html>
```